42crt.com - International Brand Needs A Fresh Look

New Company needing an fresh clean look. 42crts.com.au

Product: SSLs

Brands: Varnolux, TerraBond, Plimmo, SwiftCRT

Encourage all designers that can deliver a clean and fresh design with a touch of imagination.

We don't want this to be your typical boring ssl reseller site, we want the whole process to be fast and transparent. We welcome your design ideas.

Unrelated site designs we like:
www.wideshopfront.com, www.plorvix.com

Backend - Orlisk Run

Pages to design:

Home Page - see examples above. looking for fresh ideas!!

Product Page - try and avoid grids or boring/usual ways to display ssl information and product info. looking for fresh ideas!!

Contact us page

Checkout - using orlisk run, so not sure how much we can customise on this page

we had thought about an idea using an input box on the home page - that looks like a browser bar where they enter the url they are purchasing for - different way to display this and get them to interact with the site. when they click find SSLs button the options display below.... just a thought!

Please ask any questions you have.

Thanks.
Marcus

Requirements
Must have
• logos of the brands we are selling and we are platinum partners of each.

logo's of brands that use our ssls - please choose some example ones.

Nice to have
• nice to have a most popular either for each one or across the site

```html
<!DOCTYPE html>
<html lang="en">
<head>
<meta charset="utf-8">
<title>42crt.com – SSL certificates</title>
<link href="https://fonts.googleapis.com/css2?family=Open+Sans:wght@300;400;600;700&family=Noto+Serif:ital@1&display=swap" rel="stylesheet">
<style>
:root{
  --teal:#1ab3b6;
  --red:#e61e2a;
  --ink:#2b2f33;
  --text:#4a4f55;
  --muted:#7d838a;
  --rule:#e3e6e8;
  --paper:#ffffff;
  --cta-band:#eef2f3;
  --footer:#414a54;
  --footer-deep:#38414a;
  --footer-text:#c3c9cf;
  --footer-dim:#8c949c;
}
*{box-sizing:border-box;margin:0;padding:0}
html,body{width:1200px;height:2449px;overflow:hidden}
body{font-family:"Open Sans",Arial,sans-serif;color:var(--text);background:var(--paper);position:relative}
a{color:inherit;text-decoration:none}

/* header */
.site-header{position:absolute;top:0;left:0;width:1200px;height:98px;background:var(--paper)}
.brand{position:absolute;left:153px;top:43px;font-size:25px;line-height:30px;font-weight:700;color:var(--ink);display:flex;align-items:center;gap:10px}
.brand-mark{width:26px;height:26px;border-radius:50%;background:var(--red)}
.main-nav a{position:absolute;top:55px;font-size:14px;line-height:18px;color:var(--text)}
.main-nav .is-active{color:var(--teal)}
.account-link{position:absolute;top:54px;display:flex;align-items:center;gap:8px;font-size:14px;line-height:18px;font-weight:600;color:var(--text)}
.account-link.cart{color:var(--teal)}

/* hero */
.hero{position:absolute;top:98px;left:0;width:1200px;height:563px;overflow:hidden}
.hero-photo{position:absolute;inset:0;background:
  radial-gradient(ellipse 360px 420px at 860px 300px,#c9d5da 0%,rgba(201,213,218,0) 70%),
  radial-gradient(ellipse 260px 300px at 880px 220px,#b88c6e 0%,rgba(184,140,110,0) 70%),
  linear-gradient(90deg,#f1eeec 0%,#e8e2de 45%,#ddd6d2 70%,#ebe7e5 100%)}
.hero-title{position:absolute;left:130px;top:171px;font-size:50px;font-weight:300;line-height:58px;color:var(--ink);letter-spacing:-.5px}
.hero-title strong{font-weight:600}
.domain-search{position:absolute;left:130px;top:401px}
.domain-input{position:absolute;left:0;top:0;width:399px;height:50px;border-radius:3px;background:#fff;border:1px solid #e2e2e2;padding:0 20px;font-size:16px;color:#b6b9bc;display:flex;align-items:center}
.btn{display:inline-flex;align-items:center;justify-content:center;border-radius:3px;color:#fff;font-family:inherit}
.btn-red{background:var(--red)}
.btn-teal{background:var(--teal)}
.domain-submit{position:absolute;left:420px;top:0;width:170px;height:50px;font-size:16px}

/* protection band */
.protection{position:absolute;top:661px;left:0;width:1200px;height:338px;background:var(--teal);color:#fff}
.protection h2{position:absolute;top:46px;width:100%;text-align:center;font-size:29px;line-height:40px;font-weight:600}
.protection .divider{position:absolute;top:108px;left:460px;width:280px;height:1px;background:rgba(255,255,255,.35)}
.benefit{position:absolute;top:138px;width:300px}
.benefit h3{display:flex;align-items:center;gap:12px;font-size:17px;line-height:26px;font-weight:700;margin-bottom:12px}
.benefit p{font-size:13px;line-height:20px;hyphens:auto}

/* leaders */
.leaders-title{position:absolute;top:1033px;left:130px;font-size:25px;line-height:36px;font-weight:600;color:var(--ink)}
.rule{position:absolute;height:1px;background:var(--rule)}
.vendor{position:absolute;top:1120px;width:222px}
.vendor-name{height:50px;display:flex;align-items:center;font-size:28px;font-weight:600;color:var(--ink);letter-spacing:-.3px}
.vendor h4{margin-top:34px;font-size:15px;line-height:20px;font-weight:700;color:var(--ink)}
.vendor p{margin-top:18px;font-size:13px;line-height:20px;color:var(--muted);height:80px}
.vendor .btn{margin-top:32px;width:119px;height:40px;font-size:13px}

/* why + testimonial */
.section-head{position:absolute;top:1491px;font-size:17px;line-height:24px;font-weight:700;color:var(--ink)}
.why-copy{position:absolute;top:1546px;left:130px;width:455px;font-size:13px;line-height:20.5px;color:var(--muted)}
.avatar{position:absolute;left:610px;top:1547px;width:98px;height:98px;border-radius:50%;background:radial-gradient(circle at 50% 45%,#d9b89c 0%,#a98064 60%,#8e6b55 100%)}
.quote{position:absolute;left:731px;top:1546px;width:345px;font-family:"Noto Serif",Georgia,serif;font-style:italic;font-size:13px;line-height:20px;color:var(--text)}
.quote-author{position:absolute;left:731px;top:1633px;font-size:14px;line-height:20px;font-weight:700;color:var(--ink)}
.quote-author span{font-weight:400;color:var(--teal);font-size:12px}
.quote-site{position:absolute;left:731px;top:1655px;font-size:12px;line-height:18px;color:var(--muted)}
.slider-dots{position:absolute;left:803px;top:1689px;display:flex;gap:5px}
.slider-dots i{width:10px;height:10px;border-radius:50%;background:#8b9096}
.slider-dots i.is-active{background:var(--teal)}

/* help band */
.help-band{position:absolute;top:1769px;left:0;width:1200px;height:121px;background:var(--cta-band)}
.help-band p{position:absolute;left:130px;top:45px;font-size:21px;line-height:30px;color:var(--ink)}
.help-band .btn{position:absolute;left:889px;top:42px;width:142px;height:39px;font-size:16px}

/* footer */
.site-footer{position:absolute;top:1890px;left:0;width:1200px;height:559px;background:linear-gradient(180deg,var(--footer) 0%,var(--footer-deep) 100%);color:var(--footer-text)}
.footer-col{position:absolute;top:52px;width:220px}
.footer-col h5{font-size:15px;line-height:24px;font-weight:700;color:#fff;margin-bottom:22px}
.footer-col li{list-style:none;font-size:13px;line-height:28px}
.footer-col .support{color:var(--teal)}
.footer-rule{position:absolute;top:427px;left:130px;width:940px;height:1px;background:rgba(255,255,255,.08)}
.footer-partner{position:absolute;top:481px;left:130px;font-size:19px;line-height:26px;font-weight:600;color:var(--footer-dim)}
.copyright{position:absolute;top:487px;left:276px;font-size:12px;line-height:16px;color:#9aa1a8}
.footer-brand{position:absolute;top:480px;left:946px;font-size:20px;line-height:28px;font-weight:700;color:#d7dbdf;display:flex;align-items:center;gap:8px}
.footer-brand .brand-mark{width:22px;height:22px;background:var(--footer-dim)}
</style>
</head>
<body>

<header class="site-header">
  <div class="brand"><span class="brand-mark"></span>42CRT.com</div>
  <nav class="main-nav">
    <a class="is-active" style="left:379px">Home</a>
    <a style="left:443px">About Us</a>
    <a style="left:527px">SSL Certificates</a>
    <a style="left:650px">Support</a>
    <a style="left:727px">Contact</a>
  </nav>
  <a class="account-link" style="left:831px"><svg width="16" height="16" viewBox="0 0 16 16"><circle cx="8" cy="5" r="4" fill="#777"/><path d="M0 16c0-5 4-6 8-6s8 1 8 6z" fill="#777"/></svg>My Account</a>
  <a class="account-link cart" style="left:957px"><svg width="20" height="16" viewBox="0 0 20 16"><path d="M0 1h4l3 9h10l2-7H6" fill="none" stroke="#555" stroke-width="2"/><circle cx="8" cy="14" r="1.6" fill="#555"/><circle cx="16" cy="14" r="1.6" fill="#555"/></svg>My Cart</a>
</header>

<section class="hero">
  <div class="hero-photo" role="img" aria-label="Photo of a smiling woman in a turquoise blouse holding glasses, in a bright blurred office"></div>
  <h1 class="hero-title">Increase security and<br>trust of your business<br>with an <strong>SSL certificate</strong></h1>
  <form class="domain-search">
    <div class="domain-input">Your Domain name</div>
    <div class="btn btn-red domain-submit">Get SSL Options</div>
  </form>
</section>

<section class="protection">
  <h2>How does an SSL certificate protect your business?</h2>
  <div class="divider"></div>
  <div class="benefit" style="left:130px">
    <h3><svg width="22" height="26" viewBox="0 0 22 26"><path d="M5 12V8a6 6 0 0 1 12 0v4" fill="none" stroke="#fff" stroke-width="3"/><rect x="1" y="12" width="20" height="14" rx="2" fill="#fff"/></svg>Display signs of protection</h3>
    <p>Lorem ipsum dolor sit amet, consetetur sadipscing elitr, sed diam nonumy amet, consetetur sadipscing elitr, sed diam non eirmod tempor invidunt ut labore et dolore.</p>
  </div>
  <div class="benefit" style="left:450px">
    <h3><svg width="22" height="26" viewBox="0 0 22 26"><path d="M11 4a7 7 0 0 0-4 12.7V20h8v-3.3A7 7 0 0 0 11 4z" fill="none" stroke="#fff" stroke-width="2.2"/><rect x="7.5" y="22" width="7" height="2.5" fill="#fff"/><path d="M11 0v2M1 10h2M19 10h2M3.5 3.5l1.4 1.4M18.5 3.5l-1.4 1.4" stroke="#fff" stroke-width="1.6"/></svg>Data encryption</h3>
    <p>Lorem ipsum dolor sit amet, consetetur sadipscing elitr, sed diam nonumy amet, consetetur sadipscing elitr, sed diam non eirmod tempor invidunt ut labore et dolore.</p>
  </div>
  <div class="benefit" style="left:770px">
    <h3><svg width="22" height="26" viewBox="0 0 22 26"><path d="M11 1l10 4v7c0 7-5 11-10 13C6 23 1 19 1 12V5z" fill="#fff"/><text x="11" y="18" text-anchor="middle" font-size="13" font-weight="700" fill="#1ab3b6" font-family="Open Sans, sans-serif">$</text></svg>Protect your customers</h3>
    <p>Lorem ipsum dolor sit amet, consetetur sadipscing elitr, sed diam nonumy amet, consetetur sadipscing elitr, sed diam non eirmod tempor invidunt ut labore et dolore.</p>
  </div>
</section>

<h2 class="leaders-title">Leaders in SSL certificate</h2>
<div class="rule" style="top:1089px;left:130px;width:940px"></div>

<article class="vendor" style="left:130px">
  <div class="vendor-name">Varnolux</div>
  <h4>Lorem ipsum dolor sit amet, consetetur sadipscing.</h4>
  <p>Duis autem vel eum iriure dolor in hendrerit in vulputate velit esse molestie consequat, vel illum dolore.</p>
  <a class="btn btn-red">Learn More</a>
</article>
<article class="vendor" style="left:369px">
  <div class="vendor-name">Plimmo</div>
  <h4>Lorem ipsum dolor sit amet, consetetur sadipscing.</h4>
  <p>Duis autem vel eum iriure dolor in hendrerit in vulputate velit esse molestie consequat, vel illum doloreugiat.</p>
  <a class="btn btn-teal">Learn More</a>
</article>
<article class="vendor" style="left:609px">
  <div class="vendor-name">SwiftCRT</div>
  <h4>Lorem ipsum dolor sit amet, consetetur sadipscing.</h4>
  <p>Duis autem vel eum iriure dolor in hendrerit in vulputate velit esse molestie consequat, vel illum dolore eu feugiat nulla.</p>
  <a class="btn btn-red">Learn More</a>
</article>
<article class="vendor" style="left:848px">
  <div class="vendor-name">TerraBond</div>
  <h4>Lorem ipsum dolor sit amet, consetetur sadipscing.</h4>
  <p>Duis autem vel eum iriure dolor in hendrerit in vulputate velit esse molestie consequat, vel illum dolore eu feugiat.</p>
  <a class="btn btn-red">Learn More</a>
</article>

<h3 class="section-head" style="left:130px">Why SSL certificate is important for your business ?</h3>
<div class="rule" style="top:1529px;left:130px;width:455px"></div>
<p class="why-copy">If you are a website owner, a designer, an IT security specialist, a privacy and legal specialist, or a running a website that collects personal customer information, getting a 128/256 BIT SSL Certificate with 99.9% browser compatibility can help protect your customers and your business. Using SSL Certificates can raise customer trust and increase website conversion. We have a wide range of security certificates to suit your budget and security requirements.</p>

<h3 class="section-head" style="left:610px">What our satisfied customers say..</h3>
<div class="rule" style="top:1529px;left:610px;width:460px"></div>
<div class="avatar" role="img" aria-label="Customer portrait photo"></div>
<blockquote class="quote">In enim justo, rhoncus ut, imperdiet a, venenatis vitae, justo. Nullam dictum felis eu pede mollis In enim justo, rhoncus ut, imperdiet a, venenatis vitae, justollam dictum felis eu pede mollis pretium.</blockquote>
<div class="quote-author">Lena Morrow , <span>Florist</span></div>
<div class="quote-site">mybloomshop.com</div>
<div class="slider-dots"><i></i><i></i><i class="is-active"></i><i></i></div>

<section class="help-band">
  <p>Do you need help to determine what works best for your business ?</p>
  <a class="btn btn-teal">Contact Us</a>
</section>

<footer class="site-footer">
  <div class="footer-col" style="left:130px">
    <h5>About Us</h5>
    <ul><li>Conseteturadipscing</li><li>Fonumy eirmod</li><li>Tempor invidunt ut l</li><li>Labore et dolore magna</li><li>Taliquyam erat,</li><li>Rosed diam voluptua.</li><li>Ativero eos et accusam</li><li>Pinjusto duo doloresg</li></ul>
  </div>
  <div class="footer-col" style="left:369px">
    <h5>SSL certificates</h5>
    <ul><li>Conseteturadipscing</li><li>Fonumy eirmod</li><li>Tempor invidunt ut l</li><li>Labore et dolore magna</li><li>Taliquyam erat,</li><li>Rosed diam voluptua.</li><li>Ativero eos et accusam</li><li>Pinjusto duo doloresg</li></ul>
  </div>
  <div class="footer-col" style="left:609px">
    <h5>Useful Links</h5>
    <ul><li>Conseteturadipscing</li><li>Fonumy eirmod</li><li>Tempor invidunt ut l</li><li>Labore et dolore magna</li><li>Taliquyam erat,</li><li>Rosed diam voluptua.</li><li>Ativero eos et accusam</li><li>Pinjusto duo doloresg</li></ul>
  </div>
  <div class="footer-col" style="left:850px">
    <h5>Contact Us</h5>
    <ul><li>(US) 1-800-555-0142</li><li>(Int) +1-555-014-2288</li><li>sales@42crt.com</li><li class="support">Contact support</li></ul>
  </div>
  <div class="footer-rule"></div>
  <div class="footer-partner">Varnolux</div>
  <div class="copyright">© Copyright 2003 - 42CRT - Site security license marketplace</div>
  <div class="footer-brand"><span class="brand-mark"></span>42CRT.com</div>
</footer>

</body>
</html>
```